Brindle Coffee, a new venture, serving our customers at functions and events, lovingly made coffee fro

www.brindlecoffee.com.au

Brindle Coffee Wordpress

The font type of our logo is: La Chatte à Maman (it can be downloaded in dafont.com)

Our trading name is Brindle Coffee. We have a passion for well made coffee and providing service with affection.

Our new logo design is being placed on the side and rear of our restored 1976 Kombi. I have attached our logo and a picture of our van. We would like to own the rights to all work on our site, with access to make additions and amendments as required with no restrictions.

We want our event business to grow through our branding of great service and lovingly made coffee.

We would like our WordPress design to be simple with a retro image that our 76 Kombi portrays as well as the hipster coffee culture of Melbourne.

To begin with we are thinking of 5 pages but are open to any suggestions you think would benefit our development. We would also like to have links to our new Facebook and Instagram pages on the bottom of each page.

Logo -Like us on Facebook
https://www.facebook.com/pages/Brindle-Coffee/9027316458810574

Logo -follow us on Instagram
Brindle_coffee

Home

Beautifully made coffee is a pleasure we should all enjoy at least once in our day.
Served from our restored 1976 Kombi we strive to provide you with an experience that will enhance your day. The care we show comes from years of training and experience as a Battista in several countries around the world.
We trust the joy of our lovingly made coffee and our retro style service will linger.
Serving great coffee at an event or function near you
Brindle Coffee.

About
Brindle coffee believes in good old fashion retro service and a high a quality product. We care that our customers receive a beautifully made coffee, chai or hot chocolate. We serve our patrons with a heartfelt smile, aiming to enhance their day.
We are fortunate enough to operate from our recently restored 1976 Kombi at functions and events around Melbourne.
You can follow us on Facebook and Instagram or book us for you special function via our contact page.
We look forward to wing able to serve you.
Brindle Coffee.

Contact Us - Safe and secure

To book us at your special function, please fill in your details below and we will respond to your query as soon as possible.

Name:

Company name:

Phone number:

Email address:

Question or comment: ( box )

Brindle Coffee
Melbourne, Victoria, Australia
Info@brindlecoffee.com.au
0461 925 274
Operating at your local function or event

Blog
Facebook and Instagram integration.

Links

We have a heartfelt passionate and eternal pursuit for exceeding expectations, providing a memorable experience. It follows that we align ourselves with organizations, business's and people who also strive for perfection in what they do, providing great services, products and customer care.

Feel free to contact some of our contacts below who we have found to be above and beyond.

The marrow group - equipment suppliers

http://www.brewtorrik.com.au

Kesh- barista consulting services

https://www.facebook.com/pages/Grand...Kesh/7719302846615098

Reedfinch Swimming Club

http://reedfinch.com.au/

Orvale Baseball Club

www.orvalebrambles.com.au/

Pelling Autos

http://www.pellingautos.com.au

Target Market(s)

Lovers of Coffee at events and functions. Customers wanting coffee catered for at their event of function

Industry/Entity Type

Cafe

Font styles to use
Other font styles liked:
• La Chatte à Maman

Requirements
Must have
• Our logo design
• 5 pages but are open to any suggestions you think would benefit our development. We would also like to have links to our new Facebook and Instagram pages on the bottom of each page.
Nice to have
• Your artistic flair and input

```html
<!DOCTYPE html>
<html lang="en">
<head>
<meta charset="utf-8">
<title>Brindle Coffee</title>
<link href="https://fonts.googleapis.com/css2?family=Oswald:wght@400;500;700&family=Open+Sans:wght@400;600&display=swap" rel="stylesheet">
<style>
:root{
  --red:#8e1b1d;
  --red-dark:#6e1214;
  --wood:#3b2316;
  --brown:#2b1a12;
  --brown-mid:#34211a;
  --footer:#3d2519;
  --bottom:#1d130e;
  --cream:#e9dcc9;
  --white:#ffffff;
  --muted:#cdbfb2;
  --black:#111111;
}
*{box-sizing:border-box;margin:0;padding:0}
html,body{width:764px;height:1200px;overflow:hidden}
body{font-family:"Open Sans",Arial,sans-serif;color:var(--white);background:var(--bottom);position:relative}
h1,h2,h3,h4,.nav a,.logo-name{font-family:"Oswald","Arial Narrow",sans-serif}

/* hero */
.hero{position:absolute;left:0;top:0;width:764px;height:300px;overflow:hidden}
.hero-photo{position:absolute;inset:0;background:
  radial-gradient(ellipse 150px 120px at 560px 175px,#f2e6d3 0,#d9b48a 45%,#8a5a36 70%,transparent 72%),
  linear-gradient(100deg,#2a170e 0%,#4a2b1a 40%,#5b3620 70%,#3a2114 100%)}
.nav{position:absolute;left:90px;top:38px;width:590px;height:34px;background:var(--red);display:flex;align-items:center;padding-left:4px}
.nav a{color:var(--white);text-decoration:none;font-size:11px;letter-spacing:.5px;padding:0 10px;line-height:34px;text-transform:uppercase}
.nav a.active{background:var(--black)}
.nav .spacer{width:96px}
.logo{position:absolute;left:342px;top:16px;width:80px;height:80px;border-radius:50%;background:var(--black);border:3px solid var(--white);display:flex;align-items:center;justify-content:center}
.logo-name{font-size:13px;color:var(--white);text-align:center;line-height:1.1;font-weight:500}
.hero-title{position:absolute;left:88px;top:168px;font-size:34px;font-weight:700;letter-spacing:1px;text-transform:uppercase}
.hero-sub{position:absolute;left:88px;top:216px;font-family:"Oswald",sans-serif;font-size:15px;line-height:22px;width:260px}
.hero-sub span{background:rgba(142,27,29,.85);padding:1px 4px}
.hero-arrows{position:absolute;left:88px;top:277px;display:flex;gap:4px}
.hero-arrows span{width:20px;height:20px;border-radius:50%;background:rgba(255,255,255,.85);display:flex;align-items:center;justify-content:center}

/* features */
.features{position:absolute;left:0;top:300px;width:764px;height:300px;background:linear-gradient(var(--red),var(--red-dark));display:flex;gap:22px;padding:64px 0 0 82px}
.feature{width:188px}
.feature h3{display:flex;align-items:center;gap:8px;font-size:14px;font-weight:400;margin-bottom:14px}
.feature h3 i{width:20px;height:20px;border-radius:50%;background:var(--white);display:inline-block}
.feature p{font-size:8.5px;line-height:13px;color:#f1d9d9;margin-bottom:20px}
.btn{display:inline-block;border:1px solid rgba(255,255,255,.7);font-size:8px;padding:3px 9px;color:var(--white)}

/* about */
.about{position:absolute;left:0;top:600px;width:764px;height:215px;background:var(--brown)}
.video{position:absolute;left:88px;top:32px;width:188px;height:164px;background:linear-gradient(135deg,#5a4a40,#c8c2ba 45%,#6b5a4c);border:4px solid #ddd}
.video-bar{position:absolute;left:0;right:0;bottom:0;height:14px;background:rgba(0,0,0,.7)}
.about-text{position:absolute;left:292px;top:28px;width:390px}
.about-text h2{font-size:15px;font-weight:400;margin-bottom:8px;text-transform:uppercase}
.about-text p{font-size:8.5px;line-height:13px;color:var(--muted);margin-bottom:14px}

/* blog */
.blog{position:absolute;left:0;top:815px;width:764px;height:160px;background:var(--brown-mid)}
.blog h2{position:absolute;left:88px;top:12px;font-size:11px;font-weight:500;text-transform:uppercase}
.blog-arrows{position:absolute;left:655px;top:12px;font-size:11px;letter-spacing:6px}
.post{position:absolute;top:36px;display:flex;gap:8px}
.post .thumb{width:112px;height:82px}
.post h4{font-size:9px;font-weight:400;text-transform:uppercase}
.post time{font-size:7.5px;color:var(--muted)}
.post p{font-size:7.5px;line-height:11px;color:var(--muted);width:86px;margin-top:6px}
.post a{font-size:7.5px;color:var(--white)}

/* footer links */
.links{position:absolute;left:0;top:975px;width:764px;height:115px;background:var(--footer);display:flex;padding:18px 0 0 88px}
.links .col{width:98px}
.links .col.wide{width:170px}
.links h4{font-size:10px;font-weight:500;text-transform:uppercase;margin-bottom:10px}
.links li{list-style:none;font-size:8px;line-height:15px;color:var(--muted)}

/* bottom */
.bottom{position:absolute;left:0;top:1090px;width:764px;height:110px;background:var(--bottom)}
.legal{position:absolute;left:88px;top:48px;font-size:8px;color:var(--muted)}
.legal p+p{margin-top:8px}
.social{position:absolute;left:608px;top:44px;display:flex;gap:4px}
.social span{width:16px;height:16px;background:#2f6fb3}
.social span:first-child{background:#3aa6d8}
.social span:last-child{background:#b8322b}
</style>
</head>
<body>

<header class="hero">
  <div class="hero-photo" role="img" aria-label="Latte with leaf art on a rustic wooden table"></div>
  <nav class="nav">
    <a class="active" href="#">Home</a>
    <a href="#">About Us</a>
    <a href="#">Services</a>
    <a href="#">Store</a>
    <span class="spacer"></span>
    <a href="#">Products</a>
    <a href="#">Blog</a>
    <a href="#">News</a>
    <a href="#">Contact Us</a>
  </nav>
  <div class="logo"><span class="logo-name">Brindle<br>Coffee</span></div>
  <h1 class="hero-title">Brindle Coffee</h1>
  <p class="hero-sub"><span>We have a passion for well made coffee</span><br><span>and providing service with affection</span></p>
  <div class="hero-arrows">
    <span><svg width="8" height="8" viewBox="0 0 8 8"><path d="M5.5 1 2.5 4l3 3" stroke="#333" stroke-width="1.5" fill="none"/></svg></span>
    <span><svg width="8" height="8" viewBox="0 0 8 8"><path d="M2.5 1l3 3-3 3" stroke="#333" stroke-width="1.5" fill="none"/></svg></span>
  </div>
</header>

<section class="features">
  <article class="feature">
    <h3><i></i>About Brindle Coffee</h3>
    <p>Lorem Ipsum is simply dummy text of the printing and typesetting industry. Lorem Ipsum has been the industry's standard dummy ...</p>
    <span class="btn">Read More</span>
  </article>
  <article class="feature">
    <h3><i></i>Service with Affection</h3>
    <p>Lorem Ipsum is simply dummy text of the printing and typesetting industry. Lorem Ipsum has been the industry's standard dummy ...</p>
    <span class="btn">Read More</span>
  </article>
  <article class="feature">
    <h3><i></i>Flavored Coffee</h3>
    <p>Lorem Ipsum is simply dummy text of the printing and typesetting industry. Lorem Ipsum has been the industry's standard dummy ...</p>
    <span class="btn">Read More</span>
  </article>
</section>

<section class="about">
  <div class="video" role="img" aria-label="Video of an espresso machine at work">
    <div class="video-bar"></div>
  </div>
  <div class="about-text">
    <h2>Serving Great Coffee</h2>
    <p>Lorem Ipsum has been the industry's standard dummy text ever since the 1500s, when an unknown printer took a galley of type and scrambled it to make a type specimen book. It has survived not only five centuries, but also the leap into electronic typesetting, remaining essentially unchanged. It was popularised in the 1960s with the release of Letraset sheets containing Lorem Ipsum passages, and more recently with desktop publishing software like Aldus PageMaker including versions of Lorem Ipsum.</p>
    <span class="btn">Read More</span>
  </div>
</section>

<section class="blog">
  <h2>Latest Blog</h2>
  <div class="blog-arrows">&lsaquo; &rsaquo;</div>
  <article class="post" style="left:88px">
    <div class="thumb" role="img" aria-label="Restored blue and white van parked outdoors" style="background:linear-gradient(#8fb6d8,#4d86b8 55%,#6d7a52)"></div>
    <div>
      <h4>Simply Dummy Text</h4>
      <time>21 aug 2015</time>
      <p>Lorem Ipsum has been the industry's standard dummy text ever since the 1500s, when an unknown printer took a</p>
      <a href="#">Read More &raquo;</a>
    </div>
  </article>
  <article class="post" style="left:395px">
    <div class="thumb" role="img" aria-label="Roasted coffee beans spilling across white" style="background:linear-gradient(135deg,#f4f1ec 35%,#6a3d22 60%,#3a1f10)"></div>
    <div>
      <h4>Simply Dummy Text</h4>
      <time>21 aug 2015</time>
      <p>Lorem Ipsum has been the industry's standard dummy text ever since the 1500s, when an unknown printer took a</p>
      <a href="#">Read More &raquo;</a>
    </div>
  </article>
</section>

<footer>
  <div class="links">
    <div class="col"><h4>Link</h4><ul><li>About us</li><li>Services</li><li>Presentation</li></ul></div>
    <div class="col"><h4>Advice</h4><ul><li>FAQs</li><li>Support</li></ul></div>
    <div class="col"><h4>Specialists</h4><ul><li>Sign Up</li><li>Forums</li><li>Promotions</li></ul></div>
    <div class="col"><h4>Agencies</h4><ul><li>Sign Up</li><li>Forums</li><li>Promotions</li></ul></div>
    <div class="col wide"><h4>Contact Us</h4><ul><li>12 Laneway Row, Melbourne 3000</li><li>Phone +61 3 9555 0142</li><li>E-mail Info@brindlecoffee.com.au</li></ul></div>
  </div>
  <div class="bottom">
    <div class="legal">
      <p>About | Disclaimer | Contact | Sitemap | Special Thanks</p>
      <p>Copyright &copy; 2015. All Rights</p>
    </div>
    <div class="social" aria-label="Social links">
      <span></span><span></span><span></span><span></span>
    </div>
  </div>
</footer>

</body>
</html>
```